6-seitiges Prospekt für Messer und Fräser für den industriellen Zuschnitt auf CNC-Flachbettanlagen
Zielgruppe
Hergestellt werden Messer und Fräser für den industriellen Zuschnitt auf CNC-Flachbettanlagen.
Den Einsatz dieser sieht man unter anderem hier: https://www.videoplattform-beispiel.de/watch?v=QxR7mLp2Zk9
Aufgabenstellung
Der Prospekt wird ein 6-Seiter (gefaltet), Seitengröße DIN A4 Hochformat und wird zweisprachig (englisch/deutsch). Er soll edel und modern anmuten.
Von euch hier soll der Titel und eine Produktseite designt werden.
Die beigestellte Datei enthält alle Beschreibungen/Texte und zu die verwendenen Bilder.

```html
<!DOCTYPE html>
<html lang="de">
<head>
<meta charset="utf-8">
<title>KlingWerk – Messer, Fräser und Zubehör</title>
<link rel="stylesheet" href="https://fonts.googleapis.com/css2?family=Montserrat:wght@300;400;700;900&family=Roboto+Condensed:wght@400;700&display=swap">
<style>
  :root {
    --stage: #e4e4e4;
    --ink-black: #0b0b0c;
    --ink-dark: #1a1a1c;
    --ink-grey: #5a5a5c;
    --steel-light: #d8d8da;
    --steel-mid: #9a9a9e;
    --panel-light: #e6e6e6;
    --brand-red: #c41a1f;
    --white: #ffffff;
    --text-dark: #222222;
  }
  * { box-sizing: border-box; margin: 0; padding: 0; }
  html, body { width: 787px; height: 1200px; overflow: hidden; }
  body {
    background: var(--stage);
    font-family: "Montserrat", Arial, sans-serif;
    position: relative;
  }

  /* ---------- shared ---------- */
  .brand {
    display: flex; align-items: center; gap: 6px;
    color: var(--white); font-weight: 700; letter-spacing: 0.2px;
  }
  .brand-square { background: var(--brand-red); display: inline-block; }
  .product-shot {
    position: absolute;
    background: linear-gradient(135deg, var(--steel-light), var(--steel-mid));
  }

  /* ---------- cover ---------- */
  .cover {
    position: absolute; left: 223px; top: 40px; width: 340px; height: 481px;
    background: linear-gradient(160deg, #303033 0%, var(--ink-black) 45%, #1c1c1e 100%);
    overflow: hidden;
    box-shadow: 0 6px 18px rgba(0,0,0,0.18);
  }
  .cover-shards { position: absolute; inset: 0; }
  .cover .brand { position: absolute; left: 22px; top: 26px; font-size: 17px; }
  .cover .brand-square { width: 14px; height: 14px; }

  .cover-title {
    position: absolute; right: 0; top: 84px; text-align: right;
    color: var(--white); font-weight: 900; line-height: 0.9;
  }
  .cover-title .line-main { display: block; font-size: 60px; letter-spacing: -1px; margin-right: -6px; }
  .cover-title .line-sub { display: block; font-size: 36px; letter-spacing: -0.5px; margin-right: -4px; }

  .cover-band {
    position: absolute; left: 56px; right: 0; top: 182px; height: 20px;
    background: var(--brand-red);
    color: var(--white); font-family: "Roboto Condensed", Arial, sans-serif;
    font-weight: 700; font-size: 9px; letter-spacing: 12px;
    display: flex; align-items: center; padding-left: 16px;
  }
  .cover-subtitle {
    position: absolute; left: 56px; top: 214px;
    color: var(--white); font-family: "Roboto Condensed", Arial, sans-serif;
    font-weight: 700; font-size: 8.5px; letter-spacing: 7px;
  }

  .cover-grid {
    position: absolute; left: 40px; right: 14px; top: 252px; height: 190px;
    display: grid; grid-template-columns: 1fr 1fr; grid-template-rows: 1fr 1fr; gap: 10px;
  }
  .cover-frame { position: relative; border: 0.6px solid var(--brand-red); }
  .shot-rotary { left: 50%; top: 50%; width: 56px; height: 56px; margin: -28px 0 0 -28px; border-radius: 50%; }
  .shot-flat { left: 22%; top: 42%; width: 70%; height: 14%; clip-path: polygon(0 60%, 100% 0, 100% 100%, 30% 100%); }
  .shot-long { left: 10%; top: 42%; width: 80%; height: 16%; clip-path: polygon(0 30%, 100% 0, 94% 100%, 0 100%); }
  .shot-router { left: 28%; top: 26%; width: 68%; height: 44%; clip-path: polygon(0 100%, 40% 45%, 100% 0, 100% 25%, 45% 70%); }

  .cover-seal {
    position: absolute; left: 22px; bottom: 18px; width: 40px; height: 40px;
    border-radius: 50%; border: 1.5px solid var(--steel-mid); background: #2a2a2c;
  }

  /* ---------- spread ---------- */
  .spread {
    position: absolute; left: 63px; top: 620px; width: 660px; height: 467px;
    display: flex; box-shadow: 0 6px 18px rgba(0,0,0,0.18);
  }
  .page { position: relative; width: 330px; height: 467px; overflow: hidden; }

  .page-intro {
    background: linear-gradient(110deg, var(--ink-black) 0%, #111 55%, #4c4c4f 100%);
    display: flex; align-items: center; justify-content: center;
  }
  .page-intro .brand { font-size: 30px; gap: 10px; }
  .page-intro .brand-square { width: 24px; height: 24px; }

  .page-product { background: var(--ink-black); }
  .page-product .cover-shards { opacity: 0.8; }
  .page-product .brand { position: absolute; right: 18px; top: 16px; font-size: 11px; gap: 4px; }
  .page-product .brand-square { width: 9px; height: 9px; }

  .section-head {
    position: absolute; left: 0; top: 56px; display: flex; align-items: center; gap: 8px;
    color: var(--white); font-size: 9px; font-weight: 300; letter-spacing: 0.5px;
  }
  .section-head .accent { width: 30px; height: 6px; background: var(--brand-red); }
  .section-head strong { font-weight: 900; }

  .category-panel {
    position: absolute; left: 0; top: 82px; width: 148px; bottom: 0;
    background: var(--panel-light);
    display: flex; flex-direction: column; justify-content: space-around;
    padding: 22px 12px 22px 10px;
  }
  .category { text-align: right; font-family: "Roboto Condensed", Arial, sans-serif; color: var(--text-dark); }
  .category .en { display: block; font-size: 5.5px; letter-spacing: 1.8px; }
  .category .de { display: block; font-size: 7px; font-weight: 700; letter-spacing: 0.3px; }

  .blade-grid {
    position: absolute; left: 160px; right: 12px; top: 88px; bottom: 18px;
    display: grid; grid-template-columns: 1fr 1fr; grid-template-rows: repeat(5, 1fr); gap: 8px 10px;
  }
  .blade-cell { position: relative; }
  .blade-cell::after {
    content: ""; position: absolute; left: 2px; bottom: 2px; width: 10px; height: 6px;
    border-left: 0.8px solid var(--brand-red); border-bottom: 0.8px solid var(--brand-red);
  }
  .blade-cell .product-shot { left: 18%; top: 18%; width: 68%; height: 52%; }
  .blade-cell .cut-single { clip-path: polygon(0 100%, 30% 40%, 100% 0, 100% 45%, 25% 100%); }
  .blade-cell .cut-double { clip-path: polygon(0 100%, 20% 45%, 100% 0, 85% 55%); }
  .blade-cell .cut-round { border-radius: 50%; top: 10%; height: 70%; left: 22%; width: 60%; }
  .blade-cell .cut-wide { clip-path: polygon(0 100%, 35% 0, 100% 0, 70% 100%); }
</style>
</head>
<body>

<section class="cover" aria-label="Titelseite">
  <svg class="cover-shards" viewBox="0 0 340 481" preserveAspectRatio="none" aria-hidden="true">
    <polygon points="150,0 340,0 340,140" fill="#ffffff" opacity="0.07"/>
    <polygon points="0,200 0,420 230,481 330,481" fill="#ffffff" opacity="0.06"/>
    <polygon points="0,300 0,481 140,481" fill="#ffffff" opacity="0.08"/>
  </svg>

  <div class="brand"><span class="brand-square"></span>KlingWerk</div>

  <h1 class="cover-title">
    <span class="line-main">BLADES</span>
    <span class="line-sub">ROUTER BITS</span>
  </h1>
  <div class="cover-band">AND ACCESOIRES</div>
  <p class="cover-subtitle">MESSER, FRÄSER UND ZUBEHÖR</p>

  <div class="cover-grid">
    <div class="cover-frame"><div class="product-shot shot-rotary" role="img" aria-label="Foto eines zehneckigen Rundmessers aus Stahl"></div></div>
    <div class="cover-frame"><div class="product-shot shot-flat" role="img" aria-label="Foto eines Flachmessers mit Schneide"></div></div>
    <div class="cover-frame"><div class="product-shot shot-long" role="img" aria-label="Foto eines langen Schleppmessers"></div></div>
    <div class="cover-frame"><div class="product-shot shot-router" role="img" aria-label="Foto eines Fräsers mit Schaft"></div></div>
  </div>

  <div class="cover-seal" role="img" aria-label="Qualitätssiegel"></div>
</section>

<section class="spread" aria-label="Produktseite Flachmesser">
  <div class="page page-intro">
    <div class="brand"><span class="brand-square"></span>KlingWerk</div>
  </div>

  <div class="page page-product">
    <svg class="cover-shards" viewBox="0 0 330 467" preserveAspectRatio="none" aria-hidden="true">
      <polygon points="200,0 330,0 330,110" fill="#ffffff" opacity="0.08"/>
    </svg>
    <div class="brand"><span class="brand-square"></span>KlingWerk</div>

    <h2 class="section-head"><span class="accent"></span>FLAT KNIFE BLADE <strong>FLACHMESSER</strong></h2>

    <div class="category-panel">
      <p class="category"><span class="en">SINGLE EDGE BLADES</span><span class="de">EINSCHNEIDIGE MESSER</span></p>
      <p class="category"><span class="en">DOUBLE EDGE BLADES</span><span class="de">DOPPELSCHNEIDIGE MESSER</span></p>
      <p class="category"><span class="en">ROUTARY BLADES</span><span class="de">ROTATIONSMESSER</span></p>
      <p class="category"><span class="en">PASSEPARTOUT BLADES</span><span class="de">PASSEPARTOUT MESSER</span></p>
      <p class="category"><span class="en">V-CUT BLADES</span><span class="de">V-CUT MESSER</span></p>
    </div>

    <div class="blade-grid">
      <div class="blade-cell"><div class="product-shot cut-single" role="img" aria-label="Einschneidiges Messer"></div></div>
      <div class="blade-cell"><div class="product-shot cut-single" role="img" aria-label="Einschneidiges Messer, Variante"></div></div>
      <div class="blade-cell"><div class="product-shot cut-double" role="img" aria-label="Doppelschneidiges Messer"></div></div>
      <div class="blade-cell"><div class="product-shot cut-double" role="img" aria-label="Doppelschneidiges Messer, Variante"></div></div>
      <div class="blade-cell"><div class="product-shot cut-round" role="img" aria-label="Zehneckiges Rotationsmesser"></div></div>
      <div class="blade-cell"><div class="product-shot cut-round" role="img" aria-label="Rundes Rotationsmesser"></div></div>
      <div class="blade-cell"><div class="product-shot cut-single" role="img" aria-label="Passepartout Messer"></div></div>
      <div class="blade-cell"><div class="product-shot cut-wide" role="img" aria-label="Passepartout Messer, breit"></div></div>
      <div class="blade-cell"><div class="product-shot cut-single" role="img" aria-label="V-Cut Messer"></div></div>
      <div class="blade-cell"><div class="product-shot cut-wide" role="img" aria-label="V-Cut Messer, breit"></div></div>
    </div>
  </div>
</section>

</body>
</html>
```